Sunny Petals: Velvet Chews

We are seeking assistance with the packaging design for our new candy range of “Sunny Petals” which is a range of heart shaped gummy candies.
The product we need help with is our VELVET CHEWS. Specifically, packaging design for the packaging (back side sealed bags) that will contain the candies (we can provide bag specs)
The candy is pink and heart shaped.
We’re wanting something brightly coloured and eye catching so it can be easily identified on shelves in stores.
In terms of colour scheme we want it to be feminine but fun. The candy has collagen and vitamin c in them and are targeted at females. We love pink, lavendar, yellow, orange, lime green etc. we’ve uploaded some inspo

```html
<!DOCTYPE html>
<html lang="en">
<head>
<meta charset="utf-8">
<title>Sunny Petals – Velvet Chews bag front</title>
<link href="https://fonts.googleapis.com/css2?family=Bebas+Neue&family=Amatic+SC:wght@700&display=swap" rel="stylesheet">
<style>
  :root {
    --backdrop: #f083a3;
    --bag-face: #ea8fab;
    --bag-face-deep: #d97896;
    --magenta: #d62a60;
    --magenta-dark: #b41f4f;
    --cream: #f6e6ed;
    --white: #ffffff;
  }
  html, body {
    margin: 0;
    padding: 0;
    width: 1200px;
    height: 1200px;
    overflow: hidden;
    background: var(--backdrop);
  }
  .canvas {
    position: relative;
    width: 1200px;
    height: 1200px;
  }
  .bag-art {
    position: absolute;
    inset: 0;
    width: 1200px;
    height: 1200px;
  }
  .brand-title {
    font-family: "Bebas Neue", "Arial Narrow", sans-serif;
    font-size: 118px;
    letter-spacing: 4px;
    fill: var(--magenta);
  }
  .product-name {
    font-family: "Amatic SC", "Comic Sans MS", cursive;
    font-weight: 700;
    font-size: 66px;
    letter-spacing: 4px;
    fill: var(--white);
  }
  .claim-text {
    font-family: "Bebas Neue", "Arial Narrow", sans-serif;
    font-size: 46px;
    letter-spacing: 1px;
    fill: var(--cream);
  }
  .weight-text {
    font-family: "Bebas Neue", "Arial Narrow", sans-serif;
    font-size: 34px;
    fill: var(--magenta);
  }
</style>
</head>
<body>
<div class="canvas">
  <svg class="bag-art" viewBox="0 0 1200 1200" xmlns="http://www.w3.org/2000/svg">
    <defs>
      <linearGradient id="faceShade" x1="0" y1="0" x2="0" y2="1">
        <stop offset="0" stop-color="var(--bag-face)"/>
        <stop offset="1" stop-color="var(--bag-face-deep)"/>
      </linearGradient>
      <radialGradient id="heroTone" cx="0.5" cy="0.45" r="0.6">
        <stop offset="0" stop-color="#e0336a"/>
        <stop offset="1" stop-color="#c9245a"/>
      </radialGradient>
      <path id="titleArc" d="M 290 610 A 310 310 0 0 1 910 610"/>
      <path id="nameArc" d="M 330 610 A 270 270 0 0 0 870 610"/>
    </defs>

    <!-- bag face -->
    <rect class="bag-face" x="230" y="110" width="740" height="980" fill="url(#faceShade)"/>
    <rect class="seal-band seal-band--top" x="230" y="110" width="740" height="62" fill="var(--magenta)"/>
    <rect class="seal-band seal-band--bottom" x="230" y="1028" width="740" height="62" fill="var(--magenta)"/>

    <!-- brand name -->
    <text class="brand-title"><textPath href="#titleArc" startOffset="50%" text-anchor="middle">SUNNY PETALS</textPath></text>

    <!-- hero artwork area -->
    <rect class="hero-illustration" role="img" aria-label="Illustration of a smiling pink candy heart with two small hearts above it, inside a dashed heart outline"
          x="410" y="420" width="380" height="400" rx="120" fill="url(#heroTone)"/>

    <!-- product name -->
    <text class="product-name"><textPath href="#nameArc" startOffset="50%" text-anchor="middle">• VELVET CHEWS •</textPath></text>

    <!-- claims pill -->
    <rect class="claims-pill" x="378" y="912" width="396" height="64" rx="14" fill="var(--magenta-dark)"/>
    <text class="claim-text" x="576" y="960" text-anchor="middle">COLLAGEN | VITAMIN C</text>

    <!-- net weight heart -->
    <path class="weight-badge" d="M 848 992 C 800 960 790 940 792 924 C 794 904 814 894 830 900 C 838 903 844 908 848 916 C 852 908 858 903 866 900 C 882 894 902 904 904 924 C 906 940 896 960 848 992 Z" fill="var(--white)"/>
    <text class="weight-text" x="848" y="950" text-anchor="middle">50g</text>
  </svg>
</div>
</body>
</html>
```